Stationery Design
Letterhead, Envelope, Business Card, Email signature design
I need single sided standard sized Business Card [3.5" x 2"]
Myriad Pro
Professional
Corisse Pallant
Brand Manager
4127 Dunford Avenue
Burnaby, B.C. V3K 8T2
604-281-7734 ext. 120
corisse@brightfernco.ca
brightfernco.ca
We are a family-owned school photography company in Western Canada. We've just had a new logo and website designed and need some new stationery.
This is the .ai file we would like to use for the stationery design. Please refer to our website, brightfernco.ca, for more information about our brand.

```html
<!DOCTYPE html>
<html lang="en">
<head>
<meta charset="utf-8">
<title>BrightFern Co – Business Card</title>
<link rel="stylesheet" href="https://fonts.googleapis.com/css2?family=Source+Sans+3:ital,wght@0,400;0,600;0,700;1,400&display=swap">
<style>
  :root {
    --backdrop: #2e2f31;
    --card: #ffffff;
    --brand-blue: #2b9fca;
    --ink-dark: #41464c;
    --ink-grey: #6d7277;
    --rule: #b9dceb;
    --decor-soft: #e6f3f9;
    --decor-mid: #d3eaf4;
  }
  * { box-sizing: border-box; margin: 0; padding: 0; }
  html, body {
    width: 1200px; height: 780px; overflow: hidden;
    background: var(--backdrop);
    font-family: "Source Sans 3", "Myriad Pro", sans-serif;
  }
  .business-card {
    position: absolute; left: 180px; top: 150px;
    width: 840px; height: 480px;
    background: var(--card);
    border-radius: 34px;
    box-shadow: 0 18px 40px rgba(0,0,0,.45);
    overflow: hidden;
  }
  .brand-symbol-area {
    position: absolute; right: -70px; top: 40px;
    width: 420px; height: 360px;
    border-radius: 50%;
    background: radial-gradient(circle at 45% 55%, var(--decor-mid) 0%, var(--decor-soft) 55%, rgba(255,255,255,0) 72%);
  }
  .brand-lockup {
    position: absolute; left: 58px; top: 62px;
    display: flex; align-items: center; gap: 16px;
  }
  .brand-lockup__square {
    width: 46px; height: 46px; background: var(--brand-blue); border-radius: 4px;
  }
  .brand-lockup__name {
    font-size: 46px; font-weight: 700; color: var(--ink-dark);
    letter-spacing: -0.5px; line-height: 1;
  }
  .holder {
    position: absolute; left: 58px; top: 186px;
    display: flex; align-items: baseline; gap: 8px;
  }
  .holder__name { font-size: 27px; font-weight: 600; color: var(--brand-blue); }
  .holder__title { font-size: 18px; font-style: italic; color: var(--ink-grey); }
  .contact-block { position: absolute; left: 58px; top: 228px; width: 560px; }
  .contact-row {
    display: grid; grid-template-columns: 200px 1fr;
    font-size: 18px; color: var(--ink-grey);
    height: 34px; align-items: center;
  }
  .contact-item { display: flex; align-items: center; gap: 9px; white-space: nowrap; }
  .contact-item svg { width: 18px; height: 18px; flex: none; }
  .rule-dashed { border-top: 2px dashed var(--rule); margin: 8px 0 8px; width: 520px; }
  .address {
    position: absolute; left: 58px; top: 412px;
    font-size: 18px; color: var(--ink-grey); letter-spacing: .2px;
  }
</style>
</head>
<body>
  <div class="business-card">
    <div class="brand-symbol-area" role="img" aria-label="Large faint brand symbol decoration"></div>

    <div class="brand-lockup">
      <span class="brand-lockup__square"></span>
      <span class="brand-lockup__name">BRIGHTFERN CO</span>
    </div>

    <div class="holder">
      <span class="holder__name">Corisse Pallant</span>
      <span class="holder__title">/ Brand Manager</span>
    </div>

    <div class="contact-block">
      <div class="contact-row">
        <span class="contact-item">
          <svg viewBox="0 0 18 18" aria-hidden="true"><rect x="5" y="1" width="8" height="16" rx="2" fill="var(--brand-blue)"/><rect x="6.5" y="3" width="5" height="9" fill="#fff"/></svg>
          604-552-9160
        </span>
        <span class="contact-item">
          <svg viewBox="0 0 18 18" aria-hidden="true"><circle cx="9" cy="9" r="8" fill="var(--brand-blue)"/><text x="9" y="13" font-size="12" font-weight="700" text-anchor="middle" fill="#fff" font-family="sans-serif">@</text></svg>
          corisse@brightfernco.ca
        </span>
      </div>
      <div class="rule-dashed"></div>
      <div class="contact-row">
        <span class="contact-item">
          <svg viewBox="0 0 18 18" aria-hidden="true"><path d="M4 2l3 3-1.6 2.2a9 9 0 0 0 5.4 5.4L13 11l3 3-2 2.5C7.5 16 2 10.5 1.5 4z" fill="var(--brand-blue)"/></svg>
          (T) 1-888-377-2051
        </span>
        <span class="contact-item">
          <svg viewBox="0 0 18 18" aria-hidden="true"><path d="M4 2l3 3-1.6 2.2a9 9 0 0 0 5.4 5.4L13 11l3 3-2 2.5C7.5 16 2 10.5 1.5 4z" fill="var(--brand-blue)"/></svg>
          604-281-7734 ext. 120
        </span>
      </div>
      <div class="contact-row">
        <span class="contact-item">
          <svg viewBox="0 0 18 18" aria-hidden="true"><rect x="4" y="1" width="10" height="6" fill="var(--brand-blue)"/><rect x="1" y="7" width="16" height="8" rx="2" fill="var(--brand-blue)"/><rect x="5" y="11" width="8" height="6" fill="#fff" stroke="var(--brand-blue)"/></svg>
          604-281-7739
        </span>
        <span class="contact-item">
          <svg viewBox="0 0 18 18" aria-hidden="true"><circle cx="9" cy="9" r="7.5" fill="none" stroke="var(--brand-blue)" stroke-width="1.6"/><ellipse cx="9" cy="9" rx="3.2" ry="7.5" fill="none" stroke="var(--brand-blue)" stroke-width="1.4"/><line x1="1.5" y1="9" x2="16.5" y2="9" stroke="var(--brand-blue)" stroke-width="1.4"/></svg>
          www.brightfernco.ca
        </span>
      </div>
      <div class="rule-dashed"></div>
    </div>

    <p class="address">4127 Dunford Avenue Burnaby, B.C. V3K 8T2</p>
  </div>
</body>
</html>
```